Young judge needs a website to publish and to connect

I would like to have a website where I can publish my articles in public law. I am judge at the Alpine Civic Review Tribunal. Therefore, the website must have a calm, friendly and fairly neutral design. Also, it should be mobile friendly and easy to use.

On my website, I want to

- publish articles such as https://www.brindlepost.example/pulse/how-win-court-tobias-wenger/ and get feedbacks from my colleagues
- generate interest for my project on 'Statutes and Society - Notes from the Chamber', a book that I would like to publish in 2020 and which brings together my publications on public law (http://www.civicnorm.example/content/english/profil/publikationen.html ).
- provide updates for my university courses on constitutional, administrative and international law.

For that purpose, I would kindly ask you to suggest a website that communicates a fresh approach to the work of a young judge in constitutional and administrative law. Please have in mind that I do not only sit on the bench, but that I also work in academia. Therefore, it should be suitable for an audience from both university and law practice. The website should replace the existing website on www.civicnorm.example that I designed when still working as a lawyer. Thank you.

Target Market(s)

Academica, law firms, courts

Industry/Entity Type

University

Contact Information for Business Card

Tobias Wenger
Judge
Alpine Civic Review Tribunal
M +41 79 5XX 8X 2X

Logo Text

Notes from the Chamber

Number of Pages Required

5+ page

Font styles to use
Sans Serif

Colors
0455a3

Requirements
Must have
• - a page where I can publish and get feedbacks
• - a page about my project on law and politics
• - a page where I can provide updates for my university courses on constitutional, administrative and international law
• - page where I can list current and planned projects
• - a collaborative, young and fresh approach
Nice to have
• - a page reserved for my colleagues at the Alpine Civic Review Tribunal where I can alert them about to possibility to collaborate (if possibly password protected) and where they may suggest what to contribute to a specific project
Should not have
• anything which might to suggest that I want to make money with it, bragging or pretentious. Do not forget: I am judge, not a barrister.

```html
<!DOCTYPE html>
<html lang="en">
<head>
<meta charset="utf-8">
<title>Tobias Wenger Rechtsanwalt</title>
<link href="https://fonts.googleapis.com/css2?family=Lato:wght@300;400;700;900&display=swap" rel="stylesheet">
<style>
:root{
  --blue:#0455a3;
  --blue-dark:#033e78;
  --navy:#052c55;
  --ink:#1d1d1f;
  --text:#555a60;
  --muted:#8b9096;
  --page:#f0f1f1;
  --white:#ffffff;
  --line:#d8dadc;
  --chip:#4a4a4a;
  --social:#8a8a8a;
}
*{box-sizing:border-box;margin:0;padding:0}
html,body{width:1200px;height:2410px;overflow:hidden}
body{font-family:"Lato",Arial,sans-serif;color:var(--ink);background:var(--page);position:relative}
.wrap{width:702px;margin:0 auto;position:relative}

/* header */
.site-header{height:45px;background:var(--white);border-bottom:1px solid #e5e7ea}
.site-header .wrap{display:flex;align-items:center;justify-content:space-between;height:45px}
.brand{font-size:15px;font-weight:400;letter-spacing:1.6px;color:var(--blue);text-transform:uppercase}
.main-nav{display:flex;gap:18px;font-size:10.5px;font-weight:700;color:var(--text)}
.main-nav .active{color:var(--blue)}

/* hero */
.hero{height:281px;position:relative;background:linear-gradient(100deg,#0a57a8 0%,#1a67b4 45%,#0b4f9a 100%);color:var(--white);text-align:center;overflow:hidden}
.hero-photo{position:absolute;inset:0;background:radial-gradient(ellipse at 20% 60%,rgba(120,160,210,.35),transparent 55%),radial-gradient(ellipse at 85% 40%,rgba(20,40,90,.45),transparent 50%)}
.hero-content{position:relative;padding-top:78px}
.hero h1{font-size:21px;font-weight:700;line-height:26px}
.hero p{font-size:14px;font-weight:300;line-height:18px;margin-top:13px}
.hero p + p{margin-top:0}
.btn{display:inline-block;background:var(--navy);color:var(--white);font-size:8.5px;font-weight:700;padding:7px 18px}
.hero .btn{margin-top:15px}

/* feature */
.feature{background:var(--white);height:312px;padding-top:21px}
.feature .wrap{display:flex;gap:13px}
.slider{width:498px;height:270px;position:relative;background:#ececec;overflow:hidden}
.slider-photo{position:absolute;left:0;top:0;width:330px;height:270px;background:linear-gradient(135deg,#e9ecef 0%,#c9ced4 40%,#3f4f6a 75%,#dfe2e6 100%)}
.slider-arrow{position:absolute;top:122px;width:24px;height:24px;border-radius:50%;background:var(--blue);display:flex;align-items:center;justify-content:center}
.slider-arrow.prev{left:13px}
.slider-arrow.next{left:258px}
.slide-card{position:absolute;left:294px;top:11px;width:196px;height:248px;background:var(--white);padding:18px 27px}
.slide-dots{display:flex;gap:3px;margin-bottom:18px}
.slide-dots span{width:16px;height:2px;background:#d4d7da}
.slide-dots span.on{background:var(--blue)}
.slide-card h2{font-size:20px;font-weight:700;line-height:21px}
.slide-card p{font-size:8.5px;color:var(--text);line-height:13px;margin-top:14px}
.slide-card a{display:block;font-size:8px;font-weight:700;color:var(--blue);margin-top:14px;text-decoration:none}
.side{width:191px;display:flex;flex-direction:column;gap:26px}
.side-story{height:151px;display:flex;background:var(--blue);color:var(--white)}
.side-photo{width:95px;background:linear-gradient(180deg,#c7d6e6 0%,#9a8a78 55%,#6d6256 100%)}
.side-story div.body{padding:10px 8px 0 13px}
.side-story h3{font-size:11px;font-weight:700;line-height:13px}
.side-story p{font-size:8.5px;line-height:12.5px;margin-top:5px}
.side-story a{display:block;font-size:8px;font-weight:700;margin-top:8px}
.newsletter{height:93px;background:var(--blue);padding:10px 11px;color:var(--white)}
.newsletter h3{font-size:11px;font-weight:700}
.newsletter .field{margin-top:8px;height:20px;background:var(--white);color:var(--ink);font-size:8px;padding:5px 6px}
.newsletter .submit{margin-top:5px;height:20px;background:var(--navy);text-align:center;font-size:8px;font-weight:700;line-height:20px}

/* section bar */
.section-bar{height:27px;background:var(--blue);color:var(--white);font-size:11px;font-weight:700;padding:0 11px;line-height:27px}
.section-bar small{font-size:9px;font-weight:700}

/* updates */
.updates{padding-top:19px}
.card-grid{display:grid;grid-template-columns:repeat(4,168px);gap:10px;margin-top:21px}
.card-grid + .card-grid{margin-top:17px}
.post-card{background:var(--white);height:271px;box-shadow:0 1px 3px rgba(0,0,0,.12);border-radius:2px;overflow:hidden}
.post-photo{height:157px}
.post-card .body{padding:11px 13px 0}
.post-card h3{font-size:11px;font-weight:700;line-height:13px;min-height:13px}
.post-card p{font-size:8.5px;color:var(--text);line-height:13px;margin-top:8px;height:48px}
.post-card .rule{width:34px;height:1px;background:var(--line);margin-top:2px}
.post-card .tag{font-size:7.5px;color:var(--muted);margin-top:5px}
.ph-dancer{background:linear-gradient(180deg,#1a1a1a,#050505)}
.ph-award{background:linear-gradient(180deg,#6d7890 0%,#2a2c34 60%,#1a1a1e 100%)}
.ph-hat{background:linear-gradient(135deg,#e9343e 0%,#b63b2f 45%,#a9d0c0 80%)}
.ph-suits{background:linear-gradient(180deg,#e6e6e6 0%,#3b3e44 55%,#2a2c30 100%)}

/* divider */
.divider{display:flex;align-items:center;margin-top:23px;gap:17px}
.divider .line{flex:1;height:2px;background:var(--blue)}
.divider .btn{padding:8px 13px}

/* recent */
.recent-grid{display:grid;grid-template-columns:repeat(3,216px);gap:27px;margin-top:21px}
.recent-photo{height:141px}
.recent-item h3{font-size:11px;font-weight:700;margin-top:16px}
.recent-item p{font-size:8.5px;color:var(--text);line-height:13px;margin-top:6px}
.ph-hand{background:linear-gradient(135deg,#151515 0%,#3a3a3c 50%,#0d0d0d 100%)}
.ph-city{background:linear-gradient(160deg,#8b939c 0%,#4d5862 45%,#2a3138 100%)}
.ph-pair{background:linear-gradient(135deg,#b9a35f 0%,#6b6b4a 45%,#d8c9a8 100%)}
.dots{display:flex;justify-content:center;gap:4px;margin-top:34px}
.dots span{width:7px;height:7px;border-radius:50%;border:1px solid var(--blue)}
.dots span.on{background:var(--blue)}

/* categories */
.categories{margin-top:33px}
.tile-grid{display:grid;grid-template-columns:repeat(3,216px);gap:24px 27px;margin-top:34px}
.tile{height:111px;position:relative}
.tile .label{position:absolute;left:0;bottom:8px;display:flex;height:19px}
.tile .label span{background:var(--chip);color:var(--white);font-size:8px;font-weight:700;line-height:19px;padding:0 8px;width:66px}
.tile .label i{width:19px;background:var(--blue);display:flex;align-items:center;justify-content:center}
.ph-c1{background:linear-gradient(180deg,#9fb6cf 0%,#5b6d82 60%,#c89a35 100%)}
.ph-c2{background:linear-gradient(135deg,#d9dde1 0%,#6a6f77 50%,#c7cbcf 100%)}
.ph-c3{background:linear-gradient(135deg,#2c3a55 0%,#8a8f98 50%,#e2e4e7 100%)}
.ph-c4{background:linear-gradient(135deg,#5f6a52 0%,#cfd3d6 50%,#3d4d5e 100%)}
.ph-c5{background:linear-gradient(135deg,#e9e9e9 0%,#b9b9b9 60%,#d5d5d5 100%)}
.ph-c6{background:linear-gradient(135deg,#3b3e43 0%,#b9bdc2 50%,#2b2d31 100%)}

/* law and politics */
.law{margin-top:32px}
.law-grid{display:grid;grid-template-columns:repeat(3,216px);gap:27px;margin-top:34px}
.law-tile{height:165px;position:relative}
.law-tile span{position:absolute;left:0;top:11px;background:var(--chip);color:var(--white);font-size:8px;font-weight:700;padding:4px 8px}
.ph-l1{background:linear-gradient(135deg,#2d4a6e 0%,#1b2f48 50%,#55657a 100%)}
.ph-l2{background:linear-gradient(135deg,#c9c9c9 0%,#3d3d3d 50%,#a7a7a7 100%)}
.ph-l3{background:linear-gradient(135deg,#efefef 0%,#d9c3b8 50%,#c23f64 100%)}

/* footer */
.site-footer{position:absolute;left:0;top:2224px;width:1200px;height:186px;background:var(--white);text-align:center}
.footer-brand{font-size:13px;letter-spacing:1.6px;color:var(--blue);margin-top:33px;text-transform:uppercase}
.footer-tag{font-size:12px;font-weight:700;margin-top:14px}
.social{display:flex;justify-content:center;gap:4px;margin-top:13px}
.social span{width:28px;height:28px;border-radius:50%;background:var(--social)}
.social span.on{background:var(--blue)}
.copyright{font-size:8px;color:var(--text);margin-top:17px}
</style>
</head>
<body>

<header class="site-header">
  <div class="wrap">
    <div class="brand">Tobias Wenger Rechtsanwalt</div>
    <nav class="main-nav">
      <span class="active">Latest Publications</span>
      <span>Law and Politics</span>
      <span>Latest Updates</span>
      <span>Current and Planned Projects</span>
    </nav>
  </div>
</header>

<section class="hero">
  <div class="hero-photo" role="img" aria-label="Blue-toned photo of colleagues working together in an office"></div>
  <div class="hero-content">
    <h1>Tobias Wenger Publications<br>Comparative Judicial Review in Europe</h1>
    <p>Commentary on the Federal Administrative Procedure Act</p>
    <p>The Election of Judges and the Rule of Law</p>
    <span class="btn">Read More Articles</span>
  </div>
</section>

<section class="feature">
  <div class="wrap">
    <div class="slider">
      <div class="slider-photo" role="img" aria-label="Photo of a senior lawyer reviewing documents at a desk"></div>
      <span class="slider-arrow prev"><svg width="8" height="10" viewBox="0 0 8 10"><path d="M6 1 2 5l4 4" fill="none" stroke="#fff" stroke-width="2"/></svg></span>
      <span class="slider-arrow next"><svg width="8" height="10" viewBox="0 0 8 10"><path d="M2 1l4 4-4 4" fill="none" stroke="#fff" stroke-width="2"/></svg></span>
      <div class="slide-card">
        <div class="slide-dots"><span></span><span></span><span></span><span class="on"></span><span></span><span></span></div>
        <h2>Lorem Ipsum is simply dummy.</h2>
        <p>Lorem Ipsum is simply dummy text of the printing and typesetting industry.Lorem Ipsum is simply dummy text of the printing and typesetting industry.</p>
        <a>Read The Business</a>
      </div>
    </div>
    <aside class="side">
      <div class="side-story">
        <div class="side-photo" role="img" aria-label="Photo of a historic courthouse facade"></div>
        <div class="body">
          <h3>Lorem Ipsum is simply dummy.</h3>
          <p>Lorem Ipsum is simply dummy text of the printing and typesetting</p>
          <a>Learn More</a>
        </div>
      </div>
      <div class="newsletter">
        <h3>Subscribe Our Newsletter</h3>
        <div class="field">Email Address</div>
        <div class="submit">Subscribe</div>
      </div>
    </aside>
  </div>
</section>

<main class="wrap">
  <section class="updates">
    <div class="section-bar">Latest Updates <small>(University Courses on Constitutional, Administrative and International Law)</small></div>
    <div class="card-grid">
      <article class="post-card"><div class="post-photo ph-dancer" role="img" aria-label="Photo of a ballet dancer on a dark stage"></div><div class="body"><h3>It's all about facts</h3><p>I have not read Hale's book when I got my first trainee job in a law firm. In fact, I was a young law</p><div class="rule"></div><div class="tag">General</div></div></article>
      <article class="post-card"><div class="post-photo ph-award" role="img" aria-label="Photo of a man in a suit holding an award"></div><div class="body"><h3>Make your brief look Italian</h3><p>This brings me to my third point.</p><div class="rule"></div><div class="tag">General</div></div></article>
      <article class="post-card"><div class="post-photo ph-hat" role="img" aria-label="Photo of a woman in a bright pink hat"></div><div class="body"><h3>Always keep a stiff upper lip</h3><p>While the look and feel of your brief should be Italian, its content should be so British it even hurts.</p><div class="rule"></div><div class="tag">General</div></div></article>
      <article class="post-card"><div class="post-photo ph-suits" role="img" aria-label="Photo of men in dark business suits"></div><div class="body"><h3>Stop short of perfection, but do stop there</h3><p>Finally, it's always a good idea to revise your brief the next day.</p><div class="rule"></div><div class="tag">General</div></div></article>
    </div>
    <div class="card-grid">
      <article class="post-card"><div class="post-photo ph-dancer" role="img" aria-label="Photo of a ballet dancer on a dark stage"></div><div class="body"><h3>It's all about facts</h3><p>I have not read Hale's book when I got my first trainee job in a law firm. In fact, I was a young law</p><div class="rule"></div><div class="tag">General</div></div></article>
      <article class="post-card"><div class="post-photo ph-award" role="img" aria-label="Photo of a man in a suit holding an award"></div><div class="body"><h3>Make your brief look Italian</h3><p>This brings me to my third point.</p><div class="rule"></div><div class="tag">General</div></div></article>
      <article class="post-card"><div class="post-photo ph-hat" role="img" aria-label="Photo of a woman in a bright pink hat"></div><div class="body"><h3>Always keep a stiff upper lip</h3><p>While the look and feel of your brief should be Italian, its content should be so British it even hurts.</p><div class="rule"></div><div class="tag">General</div></div></article>
      <article class="post-card"><div class="post-photo ph-suits" role="img" aria-label="Photo of men in dark business suits"></div><div class="body"><h3>Stop short of perfection, but do stop there</h3><p>Finally, it's always a good idea to revise your brief the next day.</p><div class="rule"></div><div class="tag">General</div></div></article>
    </div>
  </section>

  <div class="divider"><span class="line"></span><span class="btn">More Recent Articles</span><span class="line"></span></div>

  <section class="recent-grid">
    <article class="recent-item"><div class="recent-photo ph-hand" role="img" aria-label="Photo of a man in a suit offering a handshake"></div><h3>What is Lorem Ipsum?</h3><p>Lorem Ipsum is simply dummy text of the printing and typesetting industry.</p></article>
    <article class="recent-item"><div class="recent-photo ph-city" role="img" aria-label="Aerial photo of city skyscrapers"></div><h3>What is Lorem Ipsum?</h3><p>Lorem Ipsum is simply dummy text of the printing and typesetting industry.</p></article>
    <article class="recent-item"><div class="recent-photo ph-pair" role="img" aria-label="Photo of two colleagues talking outdoors in sunlight"></div><h3>What is Lorem Ipsum?</h3><p>Lorem Ipsum is simply dummy text of the printing and typesetting industry.</p></article>
  </section>
  <div class="dots"><span class="on"></span><span></span><span></span><span></span><span></span></div>

  <section class="categories">
    <div class="section-bar">Categories</div>
    <div class="tile-grid">
      <div class="tile ph-c1" role="img" aria-label="Photo of business people walking in a glass hall"><div class="label"><span>Lorem Ipsum</span><i><svg width="9" height="9" viewBox="0 0 9 9"><path d="M1 4.5h6M4.5 1.5l3 3-3 3" fill="none" stroke="#fff" stroke-width="1.4"/></svg></i></div></div>
      <div class="tile ph-c2" role="img" aria-label="Photo of people waiting on chairs by a window"><div class="label"><span>Lorem Ipsum</span><i><svg width="9" height="9" viewBox="0 0 9 9"><path d="M1 4.5h6M4.5 1.5l3 3-3 3" fill="none" stroke="#fff" stroke-width="1.4"/></svg></i></div></div>
      <div class="tile ph-c3" role="img" aria-label="Photo of a business discussion at a desk"><div class="label"><span>Lorem Ipsum</span><i><svg width="9" height="9" viewBox="0 0 9 9"><path d="M1 4.5h6M4.5 1.5l3 3-3 3" fill="none" stroke="#fff" stroke-width="1.4"/></svg></i></div></div>
      <div class="tile ph-c4" role="img" aria-label="Overhead photo of a team meeting at a table"><div class="label"><span>Lorem Ipsum</span><i><svg width="9" height="9" viewBox="0 0 9 9"><path d="M1 4.5h6M4.5 1.5l3 3-3 3" fill="none" stroke="#fff" stroke-width="1.4"/></svg></i></div></div>
      <div class="tile ph-c5" role="img" aria-label="Photo of a desk with laptop and tablet"><div class="label"><span>Lorem Ipsum</span><i><svg width="9" height="9" viewBox="0 0 9 9"><path d="M1 4.5h6M4.5 1.5l3 3-3 3" fill="none" stroke="#fff" stroke-width="1.4"/></svg></i></div></div>
      <div class="tile ph-c6" role="img" aria-label="Photo of two people in business attire"><div class="label"><span>Lorem Ipsum</span><i><svg width="9" height="9" viewBox="0 0 9 9"><path d="M1 4.5h6M4.5 1.5l3 3-3 3" fill="none" stroke="#fff" stroke-width="1.4"/></svg></i></div></div>
    </div>
  </section>

  <section class="law">
    <div class="section-bar">Law and Politics</div>
    <div class="law-grid">
      <div class="law-tile ph-l1" role="img" aria-label="Photo of colleagues in a meeting"><span>Lorem Ipsum Lorem</span></div>
      <div class="law-tile ph-l2" role="img" aria-label="Black and white overhead photo of a desk meeting"><span>Lorem Ipsum Lorem</span></div>
      <div class="law-tile ph-l3" role="img" aria-label="Photo of a woman working at a laptop"><span>Lorem Ipsum Lorem</span></div>
    </div>
  </section>
</main>

<footer class="site-footer">
  <div class="footer-brand">Tobias Wenger Rechtsanwalt</div>
  <div class="footer-tag">Expertise in Public Law</div>
  <div class="social" aria-label="Social links">
    <span aria-label="Social link"></span>
    <span class="on" aria-label="Social link"></span>
    <span aria-label="Social link"></span>
    <span aria-label="Social link"></span>
    <span aria-label="Social link"></span>
  </div>
  <div class="copyright">© 2017 - Fenner Weiss Kommunikation</div>
</footer>

</body>
</html>
```